Business card design needed

We need a business card design for our new company Velbrino Event Creations, based in Leeton NSW. We will however be serving the whole Riverina area. We plan any events like, Parties, Weddings ext. We would like to see designs that is vibrant but elegant. Mainly we would like to have our Name displayed on the front and all the other info at the back. We need a design that will catch the eye anywhere.Design FRONT AND BACK

Industry/Entity Type

Events

Contact Information for Business Card

Velbrino Event Creations
Tirsa Hallveck

0461539207
velbrino@quorvamail.com

Believe the Impossible

Requirements
Must have
• Elegant Coulors and Fonts

```html
<!DOCTYPE html>
<html lang="en">
<head>
<meta charset="utf-8">
<title>Velbrino Event Creations – Business Card</title>
<link href="https://fonts.googleapis.com/css2?family=Open+Sans:wght@400;600&display=swap" rel="stylesheet">
<style>
  :root {
    --backdrop: #2b2b2b;
    --card: #050505;
    --ghost: #363636;
    --ink: #e9e9e9;
    --teal: #2aa3b3;
  }
  * { margin: 0; padding: 0; box-sizing: border-box; }
  html, body {
    width: 1200px; height: 900px; overflow: hidden;
    background: var(--backdrop);
    font-family: "Open Sans", sans-serif;
  }
  .stage { position: relative; width: 1200px; height: 900px; }
  .card {
    position: absolute; left: 250px;
    width: 700px; height: 400px;
    background: var(--card);
    overflow: hidden;
    box-shadow: 0 12px 30px rgba(0,0,0,.45);
  }
  .card--front { top: 35px; }
  .card--back { top: 465px; }
  .ghost-word {
    position: absolute;
    color: var(--ghost);
    line-height: 1;
    font-weight: 400; letter-spacing: -2px;
    white-space: nowrap;
  }
  /* front */
  .card--front .ghost-word { font-size: 190px; }
  .card--front .ghost-word--top { left: 70px; top: 50px; }
  .card--front .ghost-word--bottom { left: 180px; top: 175px; }
  .company-name {
    position: absolute; left: 110px; top: 176px;
    color: var(--ink); font-size: 44px; font-weight: 400;
    text-shadow: 0 0 6px rgba(255,255,255,.25);
    white-space: nowrap;
  }
  .tagline {
    position: absolute; left: 340px; top: 242px;
    color: var(--teal); font-size: 26px;
    white-space: nowrap;
  }
  .edge-band {
    position: absolute; left: 0; right: 0; bottom: 0;
    height: 7px; background: var(--teal);
  }
  /* back */
  .card--back .ghost-word { font-size: 150px; }
  .card--back .ghost-word--top { left: 120px; top: -8px; }
  .card--back .ghost-word--bottom { left: 40px; top: 250px; }
  .rule {
    position: absolute; height: 2px; background: var(--teal);
  }
  .rule--upper { left: 90px; width: 430px; top: 120px; }
  .rule--lower { left: 30px; width: 620px; top: 252px; }
  .contact {
    position: absolute; left: 0; width: 620px; top: 125px;
    text-align: center; color: var(--ink);
    font-size: 26px; line-height: 40px;
  }
  .contact__name { color: var(--teal); text-transform: uppercase; letter-spacing: 1px; }
</style>
</head>
<body>
<main class="stage">
  <section class="card card--front" aria-label="Card front">
    <span class="ghost-word ghost-word--top" aria-hidden="true">Vel</span>
    <span class="ghost-word ghost-word--bottom" aria-hidden="true">brino</span>
    <h1 class="company-name">Velbrino Event Creations</h1>
    <p class="tagline">Believe the Impossible</p>
    <div class="edge-band"></div>
  </section>

  <section class="card card--back" aria-label="Card back">
    <span class="ghost-word ghost-word--top" aria-hidden="true">Vel</span>
    <span class="ghost-word ghost-word--bottom" aria-hidden="true">brino</span>
    <div class="rule rule--upper"></div>
    <div class="contact">
      <p class="contact__name">Tirsa Hallveck</p>
      <p class="contact__phone">0461539207</p>
      <p class="contact__email">velbrino@quorvamail.com</p>
    </div>
    <div class="rule rule--lower"></div>
  </section>
</main>
</body>
</html>
```